massage therapy Business Card Design

massage therapy business card
I would like a custom logo created as well.
My vision is angel wings with the WB business initials in between them.
A very simple design.
Colors preferred are light blues and greens.

Target Market(s)

Massage, Spa, fitness

Industry/Entity Type

Massage Therapy

Contact Information for Business Card

A Willow Breeze
Mara Quint
Massage Therapist and Flowing Pulse Method Practitioner
2718 Bramblewood Lane, Conway, AR 72034
501-384-6190
mara.willowbreeze@mailnest.example

Colors
abd036
33a6d7
3176b5
0255a3
0392cd
9bcb3c
cadf82

Requirements
Must have
• the logo must have angel wing.

```html
<!DOCTYPE html>
<html lang="en">
<head>
<meta charset="utf-8">
<title>A Willow Breeze – Business Card</title>
<link rel="stylesheet" href="https://fonts.googleapis.com/css2?family=Arimo:ital,wght@0,400;0,700;1,400&family=Dancing+Script:wght@400&display=swap">
<style>
  :root {
    --backdrop: #e8e8e9;
    --card: #ffffff;
    --blue-deep: #0255a3;
    --blue-mid: #3176b5;
    --blue: #0392cd;
    --blue-light: #33a6d7;
    --green: #9bcb3c;
    --green-mid: #abd036;
    --green-light: #cadf82;
    --ink: #111111;
    --band-dark: #0255a3;
  }
  * { box-sizing: border-box; margin: 0; padding: 0; }
  html, body {
    width: 1200px;
    height: 720px;
    overflow: hidden;
    background: var(--backdrop);
  }
  .business-card {
    position: absolute;
    left: 60px;
    top: 45px;
    width: 1080px;
    height: 630px;
    background: var(--card);
    overflow: hidden;
    font-family: "Arimo", Arial, sans-serif;
    color: var(--ink);
  }
  .top-band {
    position: absolute;
    left: 0; top: 0;
    width: 100%; height: 43px;
    background: linear-gradient(90deg, var(--blue-mid), var(--blue) 30%, var(--blue-light) 55%, var(--blue) 80%, var(--blue-mid));
  }
  .bottom-band {
    position: absolute;
    left: 0; bottom: 0;
    width: 100%; height: 37px;
    background: var(--band-dark);
  }
  .wing-art {
    position: absolute;
    top: 43px;
    width: 195px;
    height: 550px;
    background: linear-gradient(180deg, var(--green-light), var(--green) 55%, var(--green-light));
  }
  .wing-art--left {
    left: 0;
    border-radius: 0 180px 60px 0 / 0 320px 200px 0;
  }
  .wing-art--right {
    right: 0;
    border-radius: 180px 0 0 60px / 320px 0 0 200px;
  }
  .brand-mark {
    position: absolute;
    left: 0; right: 0;
    top: 70px;
    display: flex;
    flex-direction: column;
    align-items: center;
    gap: 14px;
  }
  .brand-name {
    font-family: "Dancing Script", cursive;
    font-weight: 400;
    font-size: 66px;
    line-height: 1.05;
    text-align: center;
    color: var(--blue);
  }
  .brand-dot {
    width: 54px;
    height: 54px;
    border-radius: 50%;
    border: 4px solid var(--green-mid);
  }
  .practitioner-name {
    position: absolute;
    left: 0; right: 0;
    top: 322px;
    text-align: center;
    font-family: "Dancing Script", cursive;
    font-weight: 400;
    font-size: 52px;
    line-height: 1;
    color: var(--blue-mid);
  }
  .role-line {
    position: absolute;
    left: 215px;
    width: 650px;
    top: 412px;
    height: 45px;
    border-top: 2px solid var(--green-mid);
    border-bottom: 2px solid var(--green-mid);
    display: flex;
    align-items: center;
    justify-content: center;
    font-style: italic;
    font-size: 21px;
  }
  .contact {
    position: absolute;
    left: 0; right: 0;
    top: 467px;
    text-align: center;
    list-style: none;
  }
  .contact li { line-height: 36px; font-size: 21px; }
  .contact .phone { font-weight: 700; font-size: 22px; }
  .contact .address, .contact .email { font-style: italic; }
</style>
</head>
<body>
  <main class="business-card">
    <div class="top-band"></div>
    <div class="wing-art wing-art--left" role="img" aria-label="Large angel wing illustration in soft green"></div>
    <div class="wing-art wing-art--right" role="img" aria-label="Large angel wing illustration in soft green"></div>

    <div class="brand-mark">
      <h1 class="brand-name">A Willow<br>Breeze</h1>
      <span class="brand-dot" aria-hidden="true"></span>
    </div>
    <h2 class="practitioner-name">Mara Quint</h2>
    <p class="role-line">Massage Therapist and Flowing Pulse Method Practitioner</p>
    <ul class="contact">
      <li class="phone">501-384-6190</li>
      <li class="address">2718 Bramblewood Lane, Conway, AR 72034</li>
      <li class="email">mara.willowbreeze@mailnest.example</li>
    </ul>

    <div class="bottom-band"></div>
  </main>
</body>
</html>
```